REAL ESTATE MAILBOX DROP FLYER

I am looking for two flyer designs. One for DL and one for A4 size. My company is a boutique real estate agency that offers a full/high quality service at a very low commission rate.

Key Phrases to be included

A4 Design should have a space for some text and a table in the center (outline below)

Target Market(s)

Home Owners

Industry/Entity Type

Real Estate Agent

Colors
0455a3

Requirements
Must have
• Eye Catching
• Bold
• high end feel
• Color pallette should match the logo
• The feel of the brochures must convey a trustworthy, high end service.
• Must be eye catching and easy to read
• Editable file formats must be supplied

```html
<!DOCTYPE html>
<html lang="en">
<head>
<meta charset="utf-8">
<title>Real Estate Agent Flyer – Keystone Lane Property</title>
<link href="https://fonts.googleapis.com/css2?family=Bebas+Neue&family=Ubuntu:wght@400;500;700&display=swap" rel="stylesheet">
<style>
  :root {
    --brand-blue: #0455a3;
    --navy: #05263f;
    --accent-red: #e5212f;
    --white: #ffffff;
  }
  * { margin: 0; padding: 0; box-sizing: border-box; }
  html, body { width: 858px; height: 1200px; overflow: hidden; background: var(--white); }
  .flyer {
    position: relative; width: 858px; height: 1200px; overflow: hidden;
    background: var(--white); font-family: "Ubuntu", sans-serif; color: var(--white);
  }
  .corner-triangle { position: absolute; top: 0; left: 0; }
  .headline {
    position: absolute; left: 38px; top: 48px;
    font-family: "Bebas Neue", sans-serif; font-size: 106px; line-height: 81px;
    color: var(--brand-blue); letter-spacing: 1px; font-weight: 400;
  }
  .brand-name {
    position: absolute; left: 462px; top: 98px; width: 222px;
    text-align: center; font-family: "Ubuntu", sans-serif; font-weight: 500;
    font-size: 26px; line-height: 31px; color: var(--navy); letter-spacing: 0.5px;
  }
  .photo { position: absolute; }
  .photo-hero { left: 30px; top: 230px; width: 798px; height: 273px;
    background: linear-gradient(100deg, #7a5a3c 0%, #a07a55 15%, #e6e6e4 24%, #f1f1ef 38%, #2f4563 48%, #cfc6b8 56%, #e9e4dc 66%, #b87a45 76%, #ddd6cb 86%, #5f7a4a 100%); }
  .photo-bedroom { left: 31px; top: 552px; width: 393px; height: 201px;
    background: linear-gradient(170deg, #eceef0 0%, #dfe1e4 40%, #f2f2f2 58%, #6d6e72 78%, #55565a 100%); }
  .photo-living { left: 434px; top: 552px; width: 393px; height: 201px;
    background: linear-gradient(170deg, #e2e2e0 0%, #c9cacb 38%, #8a5a3a 55%, #b4b5b6 70%, #9d9fa1 100%); }
  .band-blue { position: absolute; left: 0; top: 510px; width: 858px; height: 17px; background: var(--brand-blue); }
  .band-navy { position: absolute; left: 0; top: 527px; width: 858px; height: 17px; background: var(--navy); }
  .backdrop-house { position: absolute; left: 0; top: 753px; width: 803px; height: 333px;
    background: linear-gradient(180deg, #f5f6f8 0%, #e9ebee 55%, #dcdfe3 100%); }
  .info-panel { position: absolute; left: 91px; top: 763px; width: 246px; height: 313px; background: var(--navy); }
  .panel-label { position: absolute; left: 27px; font-size: 15px; letter-spacing: 0.3px; }
  .panel-label.top { top: 17px; }
  .panel-label.bottom { top: 282px; }
  .panel-rule { position: absolute; left: 20px; top: 39px; width: 206px; height: 1.5px; background: var(--white); }
  .panel-box { position: absolute; left: 18px; width: 209px; border: 1.5px solid var(--white); }
  .panel-box span { position: absolute; left: 9px; top: 4px; font-size: 15px; letter-spacing: 0.3px; }
  .panel-box.text-box { top: 52px; height: 80px; }
  .panel-box.table-box { top: 134px; height: 123px; }
  .key-heading {
    position: absolute; left: 408px; top: 779px; width: 385px; height: 37px;
    border-left: 5px solid var(--brand-blue); border-right: 5px solid var(--brand-blue);
    color: var(--brand-blue); font-weight: 700; font-size: 25px; line-height: 37px; text-align: center;
  }
  .phrase {
    position: absolute; left: 416px; width: 368px; height: 69px; border-radius: 14px;
    background: var(--navy); padding: 0 0 0 20px; font-size: 20px; line-height: 23px;
    display: flex; flex-direction: column; justify-content: center; white-space: nowrap;
  }
  .phrase.one { top: 833px; }
  .phrase.two { top: 910px; font-size: 18.5px; letter-spacing: -0.2px; }
  .phrase.three { top: 987px; }
  .highlight { color: var(--accent-red); }
  .contact-footer { position: absolute; left: 0; top: 1086px; width: 858px; height: 114px; background: var(--brand-blue); }
  .contact-title { position: absolute; left: 0; top: 8px; width: 858px; text-align: center; font-size: 18px; }
  .contact-col { position: absolute; top: 33px; font-size: 16px; line-height: 23px; }
  .contact-col.left { left: 112px; }
  .contact-col.right { left: 495px; }
  .contact-divider { position: absolute; left: 428px; top: 33px; width: 2px; height: 44px; background: var(--white); }
</style>
</head>
<body>
<main class="flyer">
  <svg class="corner-triangle" width="858" height="240" viewBox="0 0 858 240" aria-hidden="true">
    <polygon points="634,230 858,0 858,230" fill="#05263f"/>
  </svg>

  <h1 class="headline">REAL ESTATE<br>AGENT</h1>
  <div class="brand-name">KEYSTONE LANE<br>PROPERTY</div>

  <div class="photo photo-hero" role="img" aria-label="Photo of a bright open-plan kitchen and living room with wine wall and sofa"></div>
  <div class="band-blue"></div>
  <div class="band-navy"></div>
  <div class="photo photo-bedroom" role="img" aria-label="Photo of a styled bedroom with armchair and walk-in robe"></div>
  <div class="photo photo-living" role="img" aria-label="Photo of a living room with grey sofas and dining area"></div>

  <div class="backdrop-house" role="img" aria-label="Faint photo of a brick and stone family home"></div>

  <section class="info-panel">
    <span class="panel-label top">ARTWORK/LOGOS ETC</span>
    <div class="panel-rule"></div>
    <div class="panel-box text-box"><span>WRITTEN TEXT</span></div>
    <div class="panel-box table-box"><span>TABLE/INFORMATION</span></div>
    <span class="panel-label bottom">ARTWORK/LOGOS ETC</span>
  </section>

  <h2 class="key-heading">KEY PHRASES – Eye Catching</h2>
  <div class="phrase one"><span>Full Service Agency,</span><span class="highlight">1% Commission</span></div>
  <div class="phrase two"><span>Contact Marcus today on</span><span>0400 123 456 for a <span class="highlight">FREE APPRAISAL!</span></span></div>
  <div class="phrase three"><span>Save Thousands On Commissions!</span></div>

  <footer class="contact-footer">
    <div class="contact-title">CONTACT DETAILS</div>
    <div class="contact-col left">More Money in YOUR Pocket!<br>Marcus Elwood - 0400 123 456</div>
    <div class="contact-divider"></div>
    <div class="contact-col right">marcus@keystonelane.com.au<br>www.keystonelane.com.au</div>
  </footer>
</main>
</body>
</html>
```